Startup Drone Platform Company business card

We are needing a business card design for our employees. We are a startup drone platform. We are looking for a business card that has our logo on one side, with the employee/company details on the opposite side. We are looking for something that is very eye catching, modern, and bold.

Target Market(s)

This will target both drone pilots and drone businesses, along with all the industries that could utilize drone services (aerial video, aerial photos, inspections, 3d mapping, etc).

Industry/Entity Type

Business

```html
<!DOCTYPE html>
<html lang="en">
<head>
<meta charset="utf-8">
<title>Skyloft Aerial – Business Card</title>
<link href="https://fonts.googleapis.com/css2?family=Montserrat:wght@300;400;600;800&display=swap" rel="stylesheet">
<style>
  :root {
    --backdrop: #2f3d46;
    --card-black: #141414;
    --card-white: #ffffff;
    --ink: #0d0d0d;
    --teal: #2fb8c4;
    --soft-white: #e9e9e9;
  }
  * { box-sizing: border-box; margin: 0; padding: 0; }
  html, body {
    width: 1200px; height: 900px; overflow: hidden;
    background: var(--backdrop);
    font-family: "Montserrat", sans-serif;
  }
  .canvas {
    width: 1200px; height: 900px;
    display: flex; flex-direction: column;
    align-items: center; justify-content: center; gap: 56px;
  }
  .card {
    width: 580px; height: 332px;
    background: var(--card-black);
    box-shadow: 0 14px 30px rgba(0,0,0,.35);
    overflow: hidden; position: relative;
  }

  /* Details side */
  .details-card { display: flex; flex-direction: column; }
  .identity {
    background: var(--card-white);
    height: 52%;
    padding: 34px 44px 0;
  }
  .identity .first-name {
    font-weight: 800; font-size: 50px; line-height: 1; color: var(--ink);
    letter-spacing: 1px;
  }
  .identity .last-name {
    font-weight: 300; font-size: 44px; line-height: 1.05; color: var(--ink);
    letter-spacing: 1px;
  }
  .identity .role {
    margin-top: 10px; font-size: 14px; letter-spacing: 1px;
    color: var(--teal); font-weight: 300;
  }
  .identity .role strong { font-weight: 600; }

  .contacts {
    flex: 1; padding: 22px 44px; list-style: none;
    display: flex; flex-direction: column; justify-content: center; gap: 12px;
  }
  .contact-row {
    display: flex; align-items: flex-start; gap: 18px;
    color: var(--soft-white); font-size: 13px; font-weight: 300; line-height: 1.35;
  }
  .contact-row svg { width: 18px; height: 18px; flex: none; }
  .contact-row svg * { fill: none; stroke: var(--teal); stroke-width: 1.4; }

  /* Brand side */
  .brand-card {
    display: flex; flex-direction: column; align-items: center; justify-content: center;
    gap: 30px;
  }
  .brand-mark { display: flex; align-items: center; gap: 18px; }
  .brand-dot {
    width: 22px; height: 22px; border-radius: 50%; background: var(--teal);
  }
  .brand-name {
    color: var(--card-white); font-weight: 400; font-size: 30px;
    letter-spacing: 12px; text-transform: uppercase;
  }
  .brand-site {
    color: var(--teal); font-size: 14px; font-weight: 300; letter-spacing: 1px;
  }
</style>
</head>
<body>
<main class="canvas">
  <section class="card details-card">
    <header class="identity">
      <p class="first-name">ALEX</p>
      <p class="last-name">MORENO</p>
      <p class="role"><strong>DIRECTOR</strong> OPERATIONS</p>
    </header>
    <ul class="contacts">
      <li class="contact-row">
        <svg viewBox="0 0 18 18" aria-hidden="true"><rect x="2" y="4" width="14" height="10" rx="1.5"/><line x1="13" y1="6" x2="13" y2="12"/></svg>
        <span>+61 400 123 456</span>
      </li>
      <li class="contact-row">
        <svg viewBox="0 0 18 18" aria-hidden="true"><circle cx="9" cy="9" r="7"/><ellipse cx="9" cy="9" rx="3" ry="7"/><line x1="2" y1="9" x2="16" y2="9"/></svg>
        <span>alex.moreno@skyloftaerial.com</span>
      </li>
      <li class="contact-row">
        <svg viewBox="0 0 18 18" aria-hidden="true"><path d="M9 16.5 C5 11.5 3.5 9 3.5 6.8 A5.5 5.5 0 0 1 14.5 6.8 C14.5 9 13 11.5 9 16.5 Z"/><circle cx="9" cy="7" r="2"/></svg>
        <span>88 Harbour Lane 12<br>Eastgate City</span>
      </li>
    </ul>
  </section>

  <section class="card brand-card">
    <div class="brand-mark">
      <span class="brand-dot" aria-hidden="true"></span>
      <span class="brand-name">Skyloft Aerial</span>
    </div>
    <p class="brand-site">www.skyloftaerial.com</p>
  </section>
</main>
</body>
</html>
```